Business Card Design Project

Financial planning, Insurance and Real estate - Financial Services company

Contact Information for Business Card

Looking for something simple in design -
Brindlewood Capital LLC
Brindlewood Wealth Managment

```html
<!DOCTYPE html>
<html lang="en">
<head>
<meta charset="utf-8">
<title>Brindlewood Wealth Management – Business Card</title>
<link href="https://fonts.googleapis.com/css2?family=Oswald:wght@500&family=Roboto+Condensed:wght@700&family=Roboto:wght@400&display=swap" rel="stylesheet">
<style>
  :root {
    --backdrop: #e7e0d8;
    --card: #f5f2ee;
    --card-edge: #dcd5cc;
    --brand-blue: #2a7ea3;
    --name-blue: #3f7f96;
    --muted: #7b7670;
    --text: #6f6a65;
  }
  html, body {
    margin: 0;
    padding: 0;
    width: 1200px;
    height: 1047px;
    overflow: hidden;
    background: var(--backdrop);
  }
  .canvas {
    position: relative;
    width: 1200px;
    height: 1047px;
  }
  .business-card {
    position: absolute;
    left: 80px;
    top: 241px;
    width: 1040px;
    height: 565px;
    background: var(--card);
    border: 2px solid var(--card-edge);
    border-radius: 26px;
    box-sizing: border-box;
  }
  .company-heading {
    position: absolute;
    left: 56px;
    top: 48px;
    margin: 0;
    font-family: "Roboto Condensed", "Arial Narrow", sans-serif;
    font-weight: 700;
    font-size: 32px;
    color: var(--brand-blue);
    letter-spacing: 0.2px;
  }
  .person-name {
    position: absolute;
    left: 56px;
    top: 296px;
    margin: 0;
    font-family: "Oswald", "Arial Narrow", sans-serif;
    font-weight: 500;
    font-size: 56px;
    line-height: 1;
    color: var(--name-blue);
    letter-spacing: 1px;
  }
  .person-role {
    position: absolute;
    left: 56px;
    top: 362px;
    margin: 0;
    font-family: "Roboto", Arial, sans-serif;
    font-size: 24px;
    color: var(--muted);
  }
  .contact-list {
    position: absolute;
    left: 56px;
    top: 420px;
    margin: 0;
    padding: 0;
    list-style: none;
    font-family: "Roboto", Arial, sans-serif;
    font-size: 23px;
    color: var(--text);
    letter-spacing: 0.3px;
  }
  .contact-item {
    display: flex;
    align-items: center;
    height: 33px;
  }
  .contact-icon {
    width: 16px;
    height: 16px;
    margin-right: 18px;
    fill: var(--name-blue);
  }
  .brand-mark {
    position: absolute;
    left: 590px;
    top: 40px;
    width: 400px;
    height: 500px;
    display: flex;
    flex-direction: column;
    align-items: center;
  }
  .brand-circle {
    width: 340px;
    height: 340px;
    border: 16px solid var(--brand-blue);
    border-radius: 50%;
    box-sizing: border-box;
  }
  .brand-name {
    margin-top: 28px;
    font-family: "Roboto Condensed", "Arial Narrow", sans-serif;
    font-weight: 700;
    font-size: 44px;
    color: var(--brand-blue);
  }
</style>
</head>
<body>
<main class="canvas">
  <section class="business-card">
    <h1 class="company-heading">Brindlewood Wealth Management</h1>

    <h2 class="person-name">DANIEL HARROW</h2>
    <p class="person-role">Director</p>

    <ul class="contact-list">
      <li class="contact-item">
        <svg class="contact-icon" viewBox="0 0 24 24" aria-hidden="true"><path d="M6.6 10.8a15.1 15.1 0 0 0 6.6 6.6l2.2-2.2c.3-.3.7-.4 1-.2 1.1.4 2.300.6 3.600.6.6 0 1 .4 1 1V20c0 .6-.4 1-1 1A17 17 0 0 1 3 4c0-.6.4-1 1-1h3.5c.6 0 1 .4 1 1 0 1.3.2 2.5.6 3.6.1.3 0 .7-.2 1z"/></svg>
        <span>+64 21 555 01234</span>
      </li>
      <li class="contact-item">
        <svg class="contact-icon" viewBox="0 0 24 24" aria-hidden="true"><path d="M3 5h18v14H3zm2 2v.4l7 4.6 7-4.6V7zm0 2.8V17h14V9.8l-7 4.6z"/></svg>
        <span>hello@brindlewoodadvisory.com</span>
      </li>
      <li class="contact-item">
        <svg class="contact-icon" viewBox="0 0 24 24" aria-hidden="true"><path d="M12 2a10 10 0 1 0 0 20 10 10 0 0 0 0-20zm6.9 6h-2.9a15 15 0 0 0-1.4-3.6A8 8 0 0 1 18.9 8zM12 4c.8 1.2 1.5 2.5 1.9 4h-3.8c.4-1.5 1.1-2.8 1.9-4zM4.3 14a8 8 0 0 1 0-4h3.4a16 16 0 0 0 0 4zm.8 2h2.9c.3 1.3.8 2.5 1.4 3.6A8 8 0 0 1 5.1 16zM8 8H5.1a8 8 0 0 1 4.3-3.6C8.8 5.5 8.3 6.7 8 8zm4 12c-.8-1.2-1.5-2.5-1.9-4h3.8c-.4 1.5-1.1 2.8-1.9 4zm2.3-6H9.7a14 14 0 0 1 0-4h4.6a14 14 0 0 1 0 4zm.3 5.6c.6-1.1 1.1-2.3 1.4-3.6h2.9a8 8 0 0 1-4.3 3.6zm1.7-5.6a16 16 0 0 0 0-4h3.4a8 8 0 0 1 0 4z"/></svg>
        <span>brindlewoodadvisory.com</span>
      </li>
    </ul>

    <div class="brand-mark">
      <div class="brand-circle"></div>
      <div class="brand-name">Brindlewood</div>
    </div>
  </section>
</main>
</body>
</html>
```